Letterhead, business card and email signature design

I have a new company and I would like a professional letterhead, business card and email signature designed. Id like the business card to have room for a photo of the bearer. I'd also like the template to be editable so we can adapt for future members of staff etc.

```html
<!DOCTYPE html>
<html lang="en">
<head>
<meta charset="utf-8">
<title>Nimbus Links – Stationery Set</title>
<link href="https://fonts.googleapis.com/css2?family=Audiowide&family=Lato:wght@400;700&display=swap" rel="stylesheet">
<style>
  :root{
    --navy:#14335a;
    --magenta:#a51c55;
    --paper:#ffffff;
    --stage:#ece8e0;
    --ink:#5c5f66;
    --ink-soft:#7b7e85;
  }
  *{box-sizing:border-box;margin:0;padding:0}
  html,body{width:1200px;height:1200px;overflow:hidden}
  body{background:var(--stage);font-family:'Lato',sans-serif;color:var(--ink);position:relative}

  .sheet{position:absolute;background:var(--paper);overflow:hidden}

  /* brand name lockup */
  .brand{display:flex;align-items:center;gap:6px;font-family:'Lato',sans-serif;font-weight:700;color:var(--navy);letter-spacing:.04em;white-space:nowrap}
  .brand-dot{border-radius:50%;background:var(--navy);flex:none}

  /* letterhead */
  .letterhead{left:262px;top:129px;width:517px;height:733px}
  .letterhead .brand{position:absolute;left:35px;top:58px;font-size:19px}
  .letterhead .brand-dot{width:50px;height:50px}
  .lh-contact{position:absolute;right:31px;top:61px;list-style:none;font-size:5px;line-height:9.5px;color:var(--ink-soft)}
  .lh-contact li{display:flex;align-items:center;gap:6px}
  .lh-contact svg{width:5px;height:5px;fill:var(--magenta)}
  .lh-body{position:absolute;left:35px;top:176px;width:451px;font-size:8.6px;line-height:10.5px;letter-spacing:.02em}
  .lh-date{font-weight:700;font-size:8.8px}
  .lh-recipient{margin-top:10px}
  .lh-address{margin-top:4px}
  .lh-salute{margin-top:50px;font-weight:700}
  .lh-body p.text{text-align:justify;margin-top:12px}
  .lh-body p.text:first-of-type{margin-top:27px}
  .lh-body p.text + p.text{margin-top:9px}
  .lh-body p.text.spaced{margin-top:19px}
  .lh-close{margin-top:24px}
  .lh-close strong{display:block;font-weight:700}
  .lh-signature{position:absolute;left:35px;top:524px;width:140px;height:34px;background:linear-gradient(180deg,#ffffff 0%,#eceef6 100%);border-bottom:1px solid #8c90a8}

  /* business cards share one column */
  .card-front,.card-back{left:795px;width:235px;height:134px}

  /* business card front */
  .card-front{top:357px;display:flex;align-items:center;justify-content:center}
  .card-front .brand{font-size:14px}
  .card-front .brand-dot{width:40px;height:40px}

  /* shared split-colour panel */
  .split{position:absolute;left:0;top:0;bottom:0;background:linear-gradient(180deg,var(--navy) 0 49%,#fff 49% 51%,var(--magenta) 51% 100%)}
  .split-panel{position:absolute;background:var(--paper);display:flex;align-items:center;justify-content:center}
  .name{font-family:'Audiowide',sans-serif;color:var(--navy);line-height:1;white-space:nowrap}
  .role{font-family:'Audiowide',sans-serif;color:var(--magenta);line-height:1}

  /* business card back */
  .card-back{top:512px}
  .card-back .split{width:126px}
  .card-back .split-panel{left:7px;top:32px;width:112px;height:70px;border-radius:35px 12px 12px 35px}
  .card-back .brand{font-size:9px;gap:4px}
  .card-back .brand-dot{width:18px;height:18px}
  .cb-details{position:absolute;left:138px;top:50px}
  .cb-details .name{font-size:9px}
  .cb-details .role{font-size:5px;margin-top:3px;margin-left:3px}
  .cb-list{list-style:none;margin-top:6px;font-size:5.6px;line-height:8.4px;color:var(--ink-soft)}
  .cb-list li{display:flex;align-items:center;gap:6px;padding-left:3px}
  .cb-list svg{width:5px;height:5px;fill:var(--magenta)}

  /* email signature */
  .signature{left:261px;top:892px;width:519px;height:174px}
  .signature .split{width:217px}
  .signature .split-panel{left:30px;top:44px;width:176px;height:90px;border-radius:45px 18px 18px 45px}
  .signature .brand{font-size:15px}
  .signature .brand-dot{width:30px;height:30px}
  .sig-details{position:absolute;left:230px;top:60px}
  .sig-details .name{font-size:15px}
  .sig-details .role{font-size:8px;margin-top:5px;margin-left:3px}
  .sig-social{position:absolute;left:419px;top:62px;display:flex;gap:3px}
  .sig-social span{width:13px;height:13px;border-radius:50%;background:var(--magenta)}
  .sig-contact{position:absolute;left:230px;top:104px;font-size:8px;line-height:14px;color:var(--ink);display:grid;grid-template-columns:auto auto;column-gap:10px}
  .sig-contact span{display:flex;align-items:center;gap:4px;white-space:nowrap}
  .sig-contact svg{width:7px;height:7px;fill:var(--magenta)}
</style>
</head>
<body>

<svg width="0" height="0" style="position:absolute">
  <symbol id="i-phone" viewBox="0 0 10 10"><path d="M2 0.5 3.8 2.6 2.9 3.8Q4 6 6.2 7.1L7.4 6.2 9.5 8 8.4 9.5Q3.5 9 0.5 1.6Z"/></symbol>
  <symbol id="i-mail" viewBox="0 0 10 10"><path d="M0 2h10v6H0z M0 2l5 3.5L10 2" stroke="#fff" stroke-width=".8"/></symbol>
  <symbol id="i-web" viewBox="0 0 10 10"><circle cx="5" cy="5" r="4.6"/><path d="M0.4 5h9.2M5 .4v9.2M1.5 2.8h7M1.5 7.2h7" stroke="#fff" stroke-width=".7"/></symbol>
  <symbol id="i-pin" viewBox="0 0 10 10"><path d="M5 0a3.6 3.6 0 0 1 3.6 3.6C8.6 6.2 5 10 5 10S1.4 6.2 1.4 3.6A3.6 3.6 0 0 1 5 0z"/><circle cx="5" cy="3.6" r="1.3" fill="#fff"/></symbol>
</svg>

<section class="sheet letterhead">
  <div class="brand"><span class="brand-dot"></span>NIMBUS LINKS</div>
  <ul class="lh-contact">
    <li><svg><use href="#i-phone"/></svg>(+000) 555 010 2</li>
    <li><svg><use href="#i-phone"/></svg>(+000) 555 010 2</li>
    <li><svg><use href="#i-mail"/></svg>info@nimbuslinks.com</li>
    <li><svg><use href="#i-web"/></svg>www.nimbuslinks.com</li>
  </ul>
  <div class="lh-body">
    <p class="lh-date">DATE:3/5/2018</p>
    <p class="lh-recipient">Recipient`s name</p>
    <p class="lh-address">14 Meadowbank Row<br>Fairhill, ST 00412</p>
    <p class="lh-salute">Dear, Mr________</p>
    <p class="text">Lorem ipsum dolor sit amet, consectetur adipiscing elit, sed do eiusmod tempor incididunt ut labore et dolore magna aliqua. Est pellentesque elit ullamcorper dignissim cras.</p>
    <p class="text spaced">Lorem ipsum dolor sit amet, consectetur adipiscing elit, sed do eiusmod tempor incididunt ut labore et dolore magna aliqua. Pharetra et ultrices neque ornare aenean euismod. Nunc eget lorem dolor sed viverra ipsum nunc. Ac ut consequat semper viverra nam libero. Eget gravida cum sociis natoque. Pretium viverra suspendisse potenti nullam. In hendrerit gravida rutrum quisque non. Ultrices gravida dictum fusce ut placerat orci. Accumsan tortor posuere ac ut consequat semper viverra. Feugiat sed lectus vestibulum mattis.</p>
    <p class="text">Lorem ipsum dolor sit amet, consectetur adipiscing elit, sed do eiusmod tempor incididunt ut labore et dolore magna aliqua. Non arcu risus quis varius quam quisque. Tincidunt eget nullam non nisi est sit amet. Tincidunt tortor aliquam nulla facilisi cras fermentum odio eu feugiat. Id leo in vitae turpis massa sed elementum tempus egestas.</p>
    <p class="lh-close"><strong>Your Sincerely</strong>M.J Alan Ward</p>
  </div>
  <div class="lh-signature" role="img" aria-label="Handwritten signature of the sender"></div>
</section>

<section class="sheet card-front">
  <div class="brand"><span class="brand-dot"></span>NIMBUS LINKS</div>
</section>

<section class="sheet card-back">
  <div class="split">
    <div class="split-panel"><div class="brand"><span class="brand-dot"></span>NIMBUS LINKS</div></div>
  </div>
  <div class="cb-details">
    <p class="name">Your Name</p>
    <p class="role">Designation</p>
    <ul class="cb-list">
      <li><svg><use href="#i-phone"/></svg>(+000) 555 010 2</li>
      <li><svg><use href="#i-mail"/></svg>info@nimbuslinks.com</li>
      <li><svg><use href="#i-web"/></svg>www.nimbuslinks.com</li>
    </ul>
  </div>
</section>

<section class="sheet signature">
  <div class="split">
    <div class="split-panel"><div class="brand"><span class="brand-dot"></span>NIMBUS LINKS</div></div>
  </div>
  <div class="sig-details">
    <p class="name">Your Name</p>
    <p class="role">Designation</p>
  </div>
  <div class="sig-social" aria-label="Social links"><span></span><span></span><span></span><span></span></div>
  <div class="sig-contact">
    <span><svg><use href="#i-phone"/></svg>(+000) 555 010 2</span>
    <span><svg><use href="#i-mail"/></svg>info@nimbuslinks.com</span>
    <span><svg><use href="#i-pin"/></svg>27 Willow Court Lakeford, ST 00518</span>
    <span><svg><use href="#i-web"/></svg>www.nimbuslinks.com</span>
  </div>
</section>

</body>
</html>
```